Business Card Design for Software Development Company

I am looking for a business card design the incorporates my new logo (attached below).

Key information to include:
Name: Darnell Whisket
Title: CEO
Email: darnell@brovatecore.com
Phone: 418-926-7301
Website: www.brovatecore.com

NOTE: This design should be easy to edit so that we can order cards for different members of our team.

```html
<!DOCTYPE html>
<html lang="en">
<head>
<meta charset="utf-8">
<title>BrovateCore Business Card</title>
<link rel="stylesheet" href="https://fonts.googleapis.com/css2?family=Montserrat:wght@400;500;600;700&display=swap">
<style>
  :root {
    --page-bg: #ece8e2;
    --card-front: #ffffff;
    --card-back: #6e7899;
    --brand-ink: #454d66;
    --accent-orange: #e87e2f;
    --accent-red: #c8402a;
    --accent-teal: #17b39b;
    --accent-peach: #f6c08c;
    --slate-light: #a4add0;
    --slate-dark: #474e69;
    --text-dark: #1f1f24;
    --text-light: #ffffff;
    --icon-ink: #3d4459;
  }
  * { margin: 0; padding: 0; box-sizing: border-box; }
  html, body {
    width: 900px;
    height: 1200px;
    overflow: hidden;
    background: var(--page-bg);
    font-family: "Montserrat", sans-serif;
  }
  .canvas { position: relative; width: 900px; height: 1200px; }

  .card {
    position: absolute;
    width: 744px;
    height: 440px;
    border-radius: 24px;
    overflow: hidden;
  }
  .card--front { left: 79px; top: 131px; background: var(--card-front); }
  .card--back { left: 78px; top: 638px; background: var(--card-back); }

  .brand { position: absolute; display: inline-block; }
  .brand__name {
    display: block;
    font-weight: 700;
    letter-spacing: -0.5px;
    line-height: 1;
    white-space: nowrap;
  }
  .brand__tagline {
    display: block;
    margin-top: 2px;
    text-align: right;
    font-weight: 700;
    font-size: 6.5px;
    letter-spacing: 0.3px;
    text-transform: uppercase;
    white-space: nowrap;
  }
  .card--front .brand { left: 36px; top: 40px; color: var(--brand-ink); }
  .card--front .brand__name { font-size: 56px; }
  .card--back .brand { left: 27px; top: 320px; color: var(--text-light); }
  .card--back .brand__name { font-size: 60px; }

  .graphic-area { position: absolute; }
  .card--front .graphic-area {
    left: 407px; top: 134px; width: 337px; height: 306px;
    background: linear-gradient(135deg, var(--accent-red) 0%, var(--accent-orange) 40%, var(--accent-peach) 70%, var(--accent-teal) 100%);
    opacity: 0.85;
  }
  .card--back .graphic-area {
    left: 305px; top: 32px; width: 439px; height: 408px;
    background: linear-gradient(135deg, var(--slate-light) 0%, var(--slate-dark) 60%);
    opacity: 0.7;
  }

  .person { position: absolute; left: 37px; top: 162px; }
  .person__name {
    font-weight: 600;
    font-size: 27px;
    color: var(--accent-orange);
    line-height: 1.1;
  }
  .person__title {
    margin-top: 6px;
    font-size: 16px;
    color: var(--text-dark);
  }

  .address {
    position: absolute;
    left: 37px;
    top: 248px;
    font-size: 16px;
    line-height: 21px;
    color: var(--text-dark);
    font-style: normal;
  }

  .contacts {
    position: absolute;
    left: 36px;
    top: 309px;
    list-style: none;
  }
  .contacts__item {
    display: flex;
    align-items: center;
    height: 28px;
    font-size: 16px;
    color: var(--text-dark);
  }
  .contacts__icon {
    width: 15px;
    height: 15px;
    margin-right: 9px;
    fill: var(--icon-ink);
    flex: none;
  }
</style>
</head>
<body>
<main class="canvas">

  <section class="card card--front" aria-label="Card front">
    <div class="graphic-area" role="img" aria-label="Large brand symbol graphic in orange, red and teal"></div>

    <div class="brand">
      <span class="brand__name">BrovateCore</span>
      <span class="brand__tagline">A division of Brovate Group</span>
    </div>

    <div class="person">
      <div class="person__name">Darnell Whisket</div>
      <div class="person__title">CEO</div>
    </div>

    <address class="address">
      415 Kestrel Park Ave, #312<br>
      Marlowe, OH 43117
    </address>

    <ul class="contacts">
      <li class="contacts__item">
        <svg class="contacts__icon" viewBox="0 0 24 24" aria-hidden="true">
          <path d="M6.6 10.8a15.1 15.1 0 0 0 6.6 6.6l2.2-2.2a1 1 0 0 1 1-.25 11.4 11.4 0 0 0 3.6.57 1 1 0 0 1 1 1V20a1 1 0 0 1-1 1A17 17 0 0 1 3 4a1 1 0 0 1 1-1h3.5a1 1 0 0 1 1 1c0 1.25.2 2.45.57 3.57a1 1 0 0 1-.25 1z"/>
        </svg>
        418-926-7301
      </li>
      <li class="contacts__item">
        <svg class="contacts__icon" viewBox="0 0 24 24" aria-hidden="true">
          <path d="M3 5h18a1 1 0 0 1 1 1v.4l-10 6.2L2 6.4V6a1 1 0 0 1 1-1zm-1 3.7 10 6.2 10-6.2V18a1 1 0 0 1-1 1H3a1 1 0 0 1-1-1z"/>
        </svg>
        darnell@brovatecore.com
      </li>
      <li class="contacts__item">
        <svg class="contacts__icon" viewBox="0 0 24 24" aria-hidden="true">
          <path d="M12 2a10 10 0 1 0 0 20 10 10 0 0 0 0-20zm6.9 6h-3a15.6 15.6 0 0 0-1.4-3.6A8 8 0 0 1 18.9 8zM12 4c.8 1.2 1.5 2.5 1.9 4h-3.8c.4-1.5 1.1-2.8 1.9-4zM4.3 14a8.2 8.2 0 0 1 0-4h3.4a16.5 16.5 0 0 0 0 4zm.8 2h3a15.6 15.6 0 0 0 1.4 3.6A8 8 0 0 1 5.1 16zm3-8h-3a8 8 0 0 1 4.4-3.6A15.6 15.6 0 0 0 8.1 8zM12 20c-.8-1.2-1.5-2.5-1.9-4h3.8c-.4 1.5-1.1 2.8-1.9 4zm2.3-6H9.7a14.7 14.7 0 0 1 0-4h4.6a14.7 14.7 0 0 1 0 4zm.2 5.6a15.6 15.6 0 0 0 1.4-3.6h3a8 8 0 0 1-4.4 3.6zm1.8-5.6a16.5 16.5 0 0 0 0-4h3.4a8.2 8.2 0 0 1 0 4z"/>
        </svg>
        www.brovatecore.com
      </li>
    </ul>
  </section>

  <section class="card card--back" aria-label="Card back">
    <div class="graphic-area" role="img" aria-label="Large brand symbol graphic in shaded slate tones"></div>

    <div class="brand">
      <span class="brand__name">BrovateCore</span>
      <span class="brand__tagline">A division of Brovate Group</span>
    </div>
  </section>

</main>
</body>
</html>
```